Business Card Design

I need a business card for my resume writing business. I have a logo that Im not keen on anymore so I would like the business card to use my photo instead of a logo. I am for mid career and trades resumes and prefer not to do executive resumes so don't need to aim for exectives. I would like it to be colourful. I like bright sky blue and maybe some pink or purple but primarily bright sky blue. I don't like green and Im keen see a fair bit of white on the card. As I have a photo to go it, it will need to go on a white background.

Target Market(s)

mid range careers. Not executives

Industry/Entity Type

Business

Contact Information for Business Card

Wyn Marchetti
Resume Writer
Clear Path CVs
27 The Lanyard
HARWOOD NSW 2465
wyn@clearpathcvs.com.au
0417362958
www.clearpathcvs.com.au

Requirements
Nice to have
• Maybe colours similar to my website - www.clearpathcvs.com.au but not with any black on it.
Should not have
• No green or dark colours

```html
<!DOCTYPE html>
<html lang="en">
<head>
<meta charset="utf-8">
<title>Clear Path CVs – Business Card</title>
<link href="https://fonts.googleapis.com/css2?family=Arimo:wght@400&display=swap" rel="stylesheet">
<style>
  :root {
    --sky: #35a6dc;
    --ink: #111111;
    --paper: #ffffff;
    --backdrop: #e9ecef;
    --photo-light: #eef0f2;
    --photo-mid: #c9b7ae;
    --photo-dark: #6b4a3c;
  }
  html, body {
    margin: 0;
    width: 1200px;
    height: 1094px;
    overflow: hidden;
    background: var(--backdrop);
    font-family: "Arimo", Arial, sans-serif;
  }
  .card {
    position: absolute;
    left: 100px;
    top: 261px;
    width: 1000px;
    height: 572px;
    background: var(--paper);
    overflow: hidden;
    box-shadow: 0 6px 24px rgba(0,0,0,0.18);
  }
  .card__bands {
    position: absolute;
    inset: 0;
  }
  .card__photo {
    position: absolute;
    left: 20px;
    top: 120px;
    width: 440px;
    height: 452px;
    background: radial-gradient(ellipse at 45% 30%, var(--photo-mid) 0%, var(--photo-dark) 22%, var(--photo-light) 48%, var(--paper) 80%);
  }
  .card__title {
    position: absolute;
    right: 60px;
    top: 92px;
    margin: 0;
    font-size: 34px;
    font-weight: 400;
    color: var(--ink);
  }
  .brand {
    position: absolute;
    right: 60px;
    top: 180px;
    width: 350px;
    text-align: right;
    font-size: 34px;
    color: var(--sky);
    padding-bottom: 6px;
    border-bottom: 2px solid var(--sky);
  }
  .contact {
    position: absolute;
    left: 540px;
    top: 262px;
    margin: 0;
    padding: 0;
    list-style: none;
    font-size: 20px;
    color: var(--ink);
  }
  .contact__item {
    display: flex;
    align-items: flex-start;
    margin-bottom: 8px;
    line-height: 26px;
  }
  .contact__icon {
    width: 28px;
    height: 26px;
    margin-right: 26px;
    flex: none;
  }
  .contact__icon svg { display: block; }
  .card__footer-name {
    position: absolute;
    left: 470px;
    top: 500px;
    font-size: 26px;
    color: var(--paper);
  }
</style>
</head>
<body>
  <div class="card">
    <svg class="card__bands" width="1000" height="572" viewBox="0 0 1000 572" aria-hidden="true">
      <path d="M0 0 H1000 V78 Q560 140 0 58 Z" fill="var(--sky)"/>
      <path d="M0 470 Q520 440 1000 478 V572 H0 Z" fill="var(--sky)"/>
    </svg>

    <div class="card__photo" role="img" aria-label="Portrait photo of Wyn Marchetti, smiling, in a white jacket"></div>

    <h1 class="card__title">Wyn Marchetti Resume Writer</h1>
    <div class="brand">Clear Path CVs</div>

    <ul class="contact">
      <li class="contact__item">
        <span class="contact__icon">
          <svg width="28" height="30" viewBox="0 0 28 30"><path d="M14 2 C8 2 4 6 4 11 C4 18 14 28 14 28 C14 28 24 18 24 11 C24 6 20 2 14 2 Z" fill="var(--sky)"/><circle cx="14" cy="11" r="4" fill="var(--paper)"/></svg>
        </span>
        <span>27 The Lanyard<br>HARWOOD NSW 2465</span>
      </li>
      <li class="contact__item">
        <span class="contact__icon">
          <svg width="28" height="26" viewBox="0 0 28 26"><rect x="1" y="5" width="26" height="17" fill="none" stroke="var(--sky)" stroke-width="2"/><path d="M1 5 L14 15 L27 5" fill="none" stroke="var(--sky)" stroke-width="2"/></svg>
        </span>
        <span>wyn@clearpathcvs.com.au</span>
      </li>
      <li class="contact__item">
        <span class="contact__icon">
          <svg width="28" height="26" viewBox="0 0 28 26"><g fill="none" stroke="var(--sky)" stroke-width="1.6"><circle cx="14" cy="13" r="11"/><ellipse cx="14" cy="13" rx="5" ry="11"/><path d="M3 13 H25 M5 7 H23 M5 19 H23"/></g></svg>
        </span>
        <span>www.clearpathcvs.com.au</span>
      </li>
      <li class="contact__item">
        <span class="contact__icon">
          <svg width="28" height="26" viewBox="0 0 28 26"><path d="M2 9 Q14 0 26 9 L23 12 L19 10 L19 8 Q14 6 9 8 L9 10 L5 12 Z" fill="var(--sky)"/><path d="M7 13 H21 L24 24 H4 Z" fill="var(--sky)"/><circle cx="14" cy="18" r="3" fill="var(--paper)"/></svg>
        </span>
        <span>0417362958</span>
      </li>
    </ul>

    <div class="card__footer-name">Wyn Marchetti Manager</div>
  </div>
</body>
</html>
```